Zielgruppe
Erbringen von Dienstleistungen in Form Interimsmanagement in Krankenhäusern in den Bereichen IT, Medizintechnik, Projektmanagement
Zielgruppe: Vorstände, Bereichsleiter, Entscheider für IT und Medizintechnik und Kosten
Branchen: Krankenhäuser, IT, Dienstleistung
Aufgabenstellung
1) Flyer DIN A 4 6seitig (2-Bruch-Wickel-Falz)
2) Texte und grobe Layout-Vorgabe in anhängendem PDF (siehe auch 6)
3) erforderliche Fotos z.B. aus Portalen wie Bildarion Platzhalter/Preview einsetzen, die Lizenzen werden dann von mir gekauft
4) Alternativ-Vorschläge bei Bildauswahl willkommen
5) 1 Profilbild je nach Platz/Layout einbauen
6) Logo-Vorlage in diversen Formaten, kann auch noch für 300dpi aufbereitet werden (derzeit noch nicht vorhanden)
6) anhängendes Dokument gibt nur grob vor, wie so etwas aussehen könnte - Alternativ-Vorschläge willkommen

```html
<!DOCTYPE html>
<html lang="de">
<head>
<meta charset="utf-8">
<title>Vertano – Flyer Interimsmanagement</title>
<link href="https://fonts.googleapis.com/css2?family=Roboto:ital,wght@0,300;0,400;0,700;1,300;1,700;1,900&display=swap" rel="stylesheet">
<style>
  :root {
    --stage: #d9d9db;
    --paper: #f6f7f8;
    --blue: #2f86b3;
    --blue-light: #5ea6cb;
    --blue-dark: #1b5f88;
    --ink: #111418;
    --photo-warm: #e8ddd0;
    --photo-cool: #cfd2d6;
  }
  * { box-sizing: border-box; margin: 0; padding: 0; }
  html, body { width: 1200px; height: 900px; overflow: hidden; }
  body {
    background: var(--stage);
    font-family: "Roboto", Arial, sans-serif;
    display: flex; align-items: center; justify-content: center;
  }
  .flyer-spread {
    display: flex;
    width: 760px; height: 810px;
    box-shadow: 0 18px 40px rgba(0,0,0,.18);
  }
  .panel { position: relative; width: 380px; height: 810px; }

  /* Cover panel */
  .panel--cover { overflow: hidden; }
  .cover-backdrop {
    position: absolute; inset: 0;
    background: linear-gradient(160deg, #eceded 0%, #d4d6d8 45%, #e9eaeb 100%);
  }
  .cover-card {
    position: absolute; left: 44px; top: 110px;
    width: 250px; height: 400px;
    background: #fbfbfb;
    box-shadow: 0 2px 8px rgba(0,0,0,.08);
  }
  .cover-photo {
    height: 265px;
    background: linear-gradient(150deg, var(--photo-cool) 0%, #f3efe9 40%, var(--photo-warm) 100%);
  }
  .brand {
    height: 135px;
    display: flex; align-items: center; justify-content: center; gap: 10px;
  }
  .brand-dot { width: 22px; height: 22px; border-radius: 50%; background: var(--blue-dark); }
  .brand-name { font-size: 40px; font-weight: 700; color: var(--blue-dark); letter-spacing: .5px; }
  .cover-tagline {
    position: absolute; left: 60px; top: 560px;
    font-size: 19px; font-weight: 300; color: var(--blue-light);
  }
  .cover-title {
    position: absolute; left: 60px; top: 610px;
    font-size: 21px; line-height: 1.4; font-weight: 700; color: var(--blue-dark);
  }

  /* Inner panel */
  .panel--inner { background: var(--paper); padding: 48px 34px 0 38px; }
  .inner-headline {
    font-size: 30px; font-weight: 300; line-height: 1.2;
    color: var(--blue-light); text-transform: uppercase; letter-spacing: 1px;
  }
  .inner-subhead {
    margin-top: 22px;
    font-size: 19px; font-style: italic; font-weight: 300; line-height: 1.3;
    color: var(--blue-dark);
  }
  .service-block { margin-top: 34px; }
  .service-heading {
    font-size: 17px; font-weight: 300; line-height: 1.3; color: var(--blue-light);
  }
  .service-list { margin-top: 14px; padding-left: 16px; }
  .service-list li {
    font-size: 11px; line-height: 1.35; color: var(--blue-dark); margin-bottom: 8px;
  }
  .service-list li::marker { color: var(--blue-dark); }
  .contact-call {
    margin-top: 38px;
    font-size: 14px; font-style: italic; font-weight: 900; line-height: 1.4; color: var(--ink);
  }
  .contact-phone {
    margin-top: 22px;
    font-size: 14px; font-style: italic; font-weight: 900; color: var(--ink);
  }
</style>
</head>
<body>
  <main class="flyer-spread">
    <section class="panel panel--cover">
      <div class="cover-backdrop" role="img" aria-label="Unscharfes helles Büro-Interieur als Hintergrundfoto"></div>
      <div class="cover-card">
        <div class="cover-photo" role="img" aria-label="Foto: heller Empfangsbereich mit Holztheke und Grünpflanze"></div>
        <div class="brand">
          <span class="brand-dot"></span>
          <span class="brand-name">Vertano</span>
        </div>
      </div>
      <p class="cover-tagline">Ihr B2B Partner</p>
      <h1 class="cover-title">Interimsmanagement &amp;<br>Projektmanagement<br>für IT &amp; Med.Technik</h1>
    </section>

    <section class="panel panel--inner">
      <h2 class="inner-headline">Flexibel und<br>schnell zuschaltbar –<br>sofort!</h2>
      <p class="inner-subhead">Med.-Technik - Möglichkeiten<br>der Ausgestaltung</p>

      <div class="service-block">
        <h3 class="service-heading">Projekt-Koordination<br>Facilities Management (FM) -<br>IT – Medizintechnik (MT), Einkauf</h3>
        <ul class="service-list">
          <li>Abstimmung mit FM bei speziellen Baumaßnahmen für med.-technische Einrichtungen</li>
          <li>Begleitung von Rahmenvertragsverhandlungen für IT, MT und Einkauf (med. Verbrauchsmaterialien für MT-Geräte)</li>
        </ul>
      </div>

      <div class="service-block">
        <h3 class="service-heading">Compliance externer Dienstleister</h3>
        <ul class="service-list">
          <li>Abwicklung der gesamten Prozesse mit externen Dienstleistern von der Auswahl, über Verhandlungsführung,</li>
          <li>Abstimmung und Koordination mit internen Abteilungen</li>
        </ul>
      </div>

      <p class="contact-call">Haben Sie spezielle Fragestellungen?<br>Rufen Sie uns an! Wir nehmen uns Zeit für Sie!</p>
      <p class="contact-phone">Mobil 0151 247 83 016</p>
    </section>
  </main>
</body>
</html>
```